Complete Stationary Package Needed for New Dental Office ! ! !

I'm moving my dental office and would like to use my existing logo to create a new:
- Business Card (please submit Business Card designs to this project - http://tasks.artbidhub.example/task.aspx?id=514290)
- Appointment Card (submit here)
- Letterhead (submit here)
- Envelope (submit here)
My practice name (within my logo) is:
Melvin R. Tuttle, D.D.S., P.A.
Family and Cosmetic Dentistry
***Obviously you will notice that the lower leg of the "T" in my logo is a smile.
My new address and contact information is:
340 Larkspur Commons Drive, Suite 118
Cary, NC 27593
919-472-3081 (ph)
919-472-3095 (fax)
info@tuttledds.example
www.tuttledds.example
If you would like to use a tagline, I would suggest "Precision Dentistry with a Personal Touch".
I have attached my logo in numerous formats.
I have also attached 2 QR codes, one of which links to my website and the other one which links to a "Like" page for my business Chatterly page. These QR codes could be improved by putting a graphic in the middle, but I created these myself and did not know how to do this.
Thank you for your time. I look forward to seeing all of your creative ideas!
Depending on the designs, I may award 2 different winners for the Business Card project and the Stationery Project. Or if a design is really good, I will award both projects to the same designer.
Updates
Project Deadline Extended
Reason: PixelBazaar administrators recently helped me split my project into 2 projects - 1 for business card and 1 for letterhead, envelope, etc. and I would like sufficient time to receive designs and provide feedback. Thank you.
Target Market(s)
Current and prospective dental patients.
Industry/Entity Type
Dental
Requirements
Must have
- Please ensure business card has a 2-sided design.
- Please ensure that your design is "practical" for printing purposes.
Nice to have
- Improvement of QR codes by addition of graphics in the middle to differentiate them. Incorporation of QR codes into business card design, maybe on the back side? I would consider the Chatterly QR code more important than the website QR code simply because my website URL is very easy to type.
Should not have
- Please, NO "floating" or "extracted" teeth which sends an undesirable message.

```html
<!DOCTYPE html>
<html lang="en">
<head>
<meta charset="utf-8">
<title>Melvin R. Tuttle, D.D.S., P.A. — Letterhead and Envelope</title>
<link rel="stylesheet" href="https://fonts.googleapis.com/css2?family=Cinzel:wght@400;600&family=Lato:wght@400&display=swap">
<style>
  :root {
    --backdrop: #d3d3d3;
    --paper: #fafafa;
    --navy-deep: #0b1450;
    --navy: #1d3590;
    --teal: #1f9e9a;
    --ink: #1b2a6b;
    --white: #ffffff;
  }
  * { box-sizing: border-box; margin: 0; padding: 0; }
  html, body { width: 1200px; height: 777px; overflow: hidden; background: var(--backdrop); }
  .canvas { position: relative; width: 1200px; height: 777px; }

  .letterhead {
    position: absolute; left: 50px; top: 38px; width: 541px; height: 700px;
    background: var(--paper); box-shadow: 0 6px 18px rgba(0,0,0,.15);
  }
  .letterhead svg.shapes { position: absolute; inset: 0; }

  .brand { position: absolute; left: 30px; top: 30px; display: flex; align-items: flex-start; gap: 8px; }
  .brand-mark { width: 20px; height: 20px; background: var(--teal); margin-top: 1px; }
  .brand-name { font-family: "Cinzel", serif; font-weight: 600; font-size: 13px; color: var(--ink); line-height: 1.2; letter-spacing: .3px; }
  .brand-sub { font-family: "Cinzel", serif; font-size: 7.5px; color: var(--teal); letter-spacing: .6px; margin-top: 2px; }

  .contact {
    position: absolute; left: 352px; top: 20px; width: 184px;
    display: grid; grid-template-columns: 62px 1fr; gap: 10px 8px;
  }
  .contact-item { display: flex; align-items: flex-start; gap: 4px; font-family: "Lato", sans-serif; font-size: 5.4px; color: var(--white); line-height: 1.3; }
  .contact-item svg { flex: none; width: 7px; height: 7px; }

  .tagline {
    position: absolute; left: 14px; top: 662px;
    font-family: "Cinzel", serif; font-size: 10px; color: var(--white); letter-spacing: .4px;
  }

  .envelope {
    position: absolute; left: 625px; top: 270px; width: 540px; height: 235px;
    background: var(--paper); box-shadow: 0 6px 18px rgba(0,0,0,.15);
  }
  .envelope svg.shapes { position: absolute; inset: 0; }
  .envelope-url {
    position: absolute; left: 0; right: 0; top: 20px; text-align: center;
    font-family: "Cinzel", serif; font-size: 11px; letter-spacing: 3px; color: var(--white);
  }
</style>
</head>
<body>
<div class="canvas">

  <section class="letterhead" aria-label="Letterhead">
    <svg class="shapes" width="541" height="700" viewBox="0 0 541 700" aria-hidden="true">
      <defs>
        <linearGradient id="bandNavy" x1="0" y1="0" x2="1" y2="0">
          <stop offset="0" stop-color="var(--navy)"/>
          <stop offset="1" stop-color="var(--navy-deep)"/>
        </linearGradient>
      </defs>
      <!-- header band -->
      <path d="M296 0 H541 V84 H346 C322 84 314 66 308 42 C302 16 298 0 296 0 Z" fill="var(--teal)"/>
      <path d="M304 0 H541 V78 H350 C330 78 322 62 316 40 C310 16 306 0 304 0 Z" fill="url(#bandNavy)"/>
      <!-- footer band -->
      <path d="M0 646 H262 C286 646 300 668 312 700 H303 C292 672 280 652 258 652 Z" fill="var(--teal)"/>
      <path d="M0 652 H256 C278 652 292 672 304 700 H0 Z" fill="url(#bandNavy)"/>
    </svg>

    <div class="brand">
      <div class="brand-mark"></div>
      <div>
        <div class="brand-name">Melvin R. Tuttle, D.D.S., P.A.</div>
        <div class="brand-sub">Family and Cosmetic Dentistry</div>
      </div>
    </div>

    <div class="contact">
      <div class="contact-item">
        <svg viewBox="0 0 10 10"><path d="M2 1 L4 1 L4.6 3 L3.4 3.8 C4 5.2 4.8 6 6.2 6.6 L7 5.4 L9 6 L9 8 C5 8.4 1.6 5 2 1 Z" fill="var(--white)"/></svg>
        <span>919-472-3081</span>
      </div>
      <div class="contact-item">
        <svg viewBox="0 0 10 10"><path d="M5 .8 C7 .8 8.2 2.2 8.2 4 C8.2 6 5 9.4 5 9.4 C5 9.4 1.8 6 1.8 4 C1.8 2.2 3 .8 5 .8 Z" fill="var(--white)"/><circle cx="5" cy="4" r="1.2" fill="var(--navy)"/></svg>
        <span>340 Larkspur Commons Drive, Suite 118<br>Cary, NC 27593</span>
      </div>
      <div class="contact-item">
        <svg viewBox="0 0 10 10"><rect x="2.5" y="1" width="5" height="3" fill="var(--white)"/><rect x="1" y="4" width="8" height="3.5" rx=".6" fill="var(--white)"/><rect x="2.5" y="6.5" width="5" height="2.5" fill="var(--white)"/></svg>
        <span>919-472-3095</span>
      </div>
      <div class="contact-item">
        <svg viewBox="0 0 10 10"><circle cx="5" cy="5" r="4" fill="none" stroke="var(--white)" stroke-width="1"/><path d="M1 5 H9 M5 1 C3 3 3 7 5 9 C7 7 7 3 5 1" fill="none" stroke="var(--white)" stroke-width=".7"/></svg>
        <span>www.tuttledds.example<br>info@tuttledds.example</span>
      </div>
    </div>

    <p class="tagline">“Precision Dentistry with a Personal Touch”</p>
  </section>

  <section class="envelope" aria-label="Envelope">
    <svg class="shapes" width="540" height="235" viewBox="0 0 540 235" aria-hidden="true">
      <defs>
        <linearGradient id="flapNavy" x1="0" y1="0" x2="1" y2="0">
          <stop offset="0" stop-color="var(--navy)"/>
          <stop offset="1" stop-color="var(--navy-deep)"/>
        </linearGradient>
      </defs>
      <path d="M0 0 H540 V98 C532 82 522 60 500 60 H0 Z" fill="url(#flapNavy)"/>
    </svg>
    <p class="envelope-url">www.tuttledds.example</p>
  </section>

</div>
</body>
</html>
```